HML5 Web Application Design

We need a graphic design to give a HTML web application a modern look and feel. The design should be clean and neat with a metro inspired interface. All application uses vormanta controls so any experience with these would be great.
Perhaps you could also include a few screenshots of your previous work

Industry/Entity Type

Graphic Design

Requirements
Must have
• Must be HTML 5 compliant

```html
<!DOCTYPE html>
<html lang="en">
<head>
<meta charset="utf-8">
<title>Supplier Transactions – Nova</title>
<link href="https://fonts.googleapis.com/css2?family=Barlow:wght@400;500;600;700;800&display=swap" rel="stylesheet">
<style>
:root{
  --page:#d8d8d8;
  --navy:#1b3a52;
  --charcoal:#232323;
  --orange:#f26a22;
  --blue:#0a86bf;
  --row-alt:#ebebeb;
  --filter:#e5e5e5;
  --ink:#1b3a52;
  --muted:#5a5a5a;
  --tile-user:#9b0a3a;
  --tile-setting:#a33a00;
  --tile-support:#7ea100;
  --tile-events:#18a018;
  --tile-graph:#0e9e9e;
  --tile-docs:#0a579c;
  --tile-message:#a07400;
  --tile-source:#f26a22;
  --tile-refresh:#470f5c;
  --tile-library:#e8168c;
}
*{box-sizing:border-box;margin:0;padding:0}
html,body{width:1200px;height:1000px;overflow:hidden}
body{background:var(--page);font-family:"Barlow",Arial,sans-serif;position:relative}
.app{position:absolute;left:96px;top:88px;width:1000px;height:824px;background:#fff}

.topbar{position:absolute;left:0;top:0;width:1000px;height:51px;background:var(--navy)}
.brand{position:absolute;left:34px;top:7px;color:#fff;font-weight:800;font-size:34px;letter-spacing:1px}
.nav{position:absolute;top:15px;left:0;font-size:14.5px;color:#fff;letter-spacing:.2px}
.nav span{position:absolute;white-space:nowrap;line-height:22px}
.nav .active{background:var(--orange);padding:0 12px;}

.sidebar{position:absolute;left:0;top:51px;width:333px;height:773px;background:var(--navy)}
.profile{position:absolute;left:0;top:0;width:320px;height:135px;background:var(--charcoal)}
.profile-bar{position:absolute;left:0;top:135px;width:320px;height:6px;background:var(--orange)}
.avatar{position:absolute;left:19px;top:25px;width:85px;height:86px;background:linear-gradient(#dcdcdc,#bdbdbd);border:3px solid #c9c9c9}
.greeting{position:absolute;left:115px;top:26px;color:#fff;font-weight:600;font-size:13px;letter-spacing:.3px}
.profile-links{position:absolute;left:116px;top:44px;color:#9a9a9a;font-size:12px;line-height:17px;list-style:none}
.search{position:absolute;left:22px;top:156px;width:296px;height:37px;display:flex}
.search-field{flex:1;background:#fff;color:#b5b5b5;font-size:16px;padding:9px 13px}
.search-btn{width:39px;background:#5a5a5a;display:flex;align-items:center;justify-content:center}
.rail{position:absolute;left:0;top:210px;width:97px;height:527px;background:var(--blue)}
.rail svg{position:absolute;left:32px}
.tile{position:absolute;width:83px;height:83px;color:#fff;font-size:12px;text-align:center;overflow:hidden}
.tile svg{position:absolute;left:24px;top:14px}
.tile .label{position:absolute;left:0;right:0;bottom:7px;letter-spacing:.3px;white-space:nowrap}
.tile .label.compact{font-size:11px;letter-spacing:0}
.tile .badge{position:absolute;right:0;top:0;background:rgba(0,0,0,.25);font-size:12px;padding:1px 3px}

.content{position:absolute;left:358px;top:51px;width:642px}
.page-title{position:absolute;top:12px;left:0;font-size:24px;color:var(--muted);font-weight:400;letter-spacing:.4px;white-space:nowrap}
.rule{position:absolute;top:48px;left:0;width:642px;height:1px;background:#ccc}
.crumbs{position:absolute;top:55px;left:4px;display:flex;align-items:center;gap:8px;font-size:16px;color:#333}
.crumbs .current{color:var(--blue)}
.filter{position:absolute;top:78px;left:0;width:642px;height:40px;background:var(--filter);font-size:16px;color:#555}
.filter .lbl{position:absolute;top:10px}
.date{position:absolute;top:7px;width:171px;height:26px;background:#fff;border:1px solid #c8c8c8;color:#aaa;font-size:15px;padding:3px 0 0 30px}
.date .cal{position:absolute;right:-1px;top:-1px;width:24px;height:26px;background:var(--orange);display:flex;align-items:center;justify-content:center}
.grid-bar{position:absolute;top:135px;left:0;width:642px;height:6px;background:var(--orange)}
.grid{position:absolute;top:141px;left:0;width:642px;border-collapse:collapse;font-size:14px;color:var(--ink)}
.grid th{background:var(--navy);color:#fff;font-weight:500;font-size:16px;text-align:left;height:37px;padding-left:8px;border-left:1px solid #4b6477;position:relative;letter-spacing:.3px}
.grid th:first-child{border-left:none}
.grid th::after{content:"";position:absolute;right:7px;top:15px;border:5px solid transparent;border-top:7px solid #fff;border-bottom:0}
.grid th:first-child::after{border-top-color:#8a9aa8}
.grid td{height:34px;padding-left:8px}
.grid tr:nth-child(even) td{background:var(--row-alt)}
.pager{position:absolute;top:696px;left:0;width:642px;height:39px;background:var(--navy)}
.pager .count{position:absolute;left:367px;top:13px;color:#9fb0bd;font-size:12px}
.pbtn{position:absolute;top:7px;width:28px;height:27px;background:#2c2c2c;display:flex;align-items:center;justify-content:center}
.pbtn.dim{background:#3a3a3a}
.pbtn.page{background:#fff;color:var(--orange);font-size:15px}
.footer{position:absolute;top:751px;left:0;width:642px;height:22px;background:var(--navy);color:#fff;font-size:9px;padding:6px 6px;letter-spacing:.2px;white-space:nowrap}
</style>
</head>
<body>
<div class="app">
  <header class="topbar">
    <div class="brand">NOVA</div>
    <nav class="nav">
      <span style="left:216px">HOME</span>
      <span style="left:274px">PIN REQUESTS</span>
      <span style="left:388px">TRANSECTIONS</span>
      <span style="left:507px">TAX DETAILS</span>
      <span style="left:608px">USERS</span>
      <span style="left:670px">SUPLIERS</span>
      <span class="active" style="left:750px">QUEIRES</span>
      <span style="left:849px">LA STAFF QUEIRES ▾</span>
    </nav>
  </header>

  <aside class="sidebar">
    <div class="profile">
      <div class="avatar" role="img" aria-label="User profile photo placeholder"></div>
      <div class="greeting">HELLO RAVI MENON</div>
      <ul class="profile-links"><li>Edit Profile</li><li>View Profile</li><li>Logout</li></ul>
    </div>
    <div class="profile-bar"></div>
    <div class="search">
      <div class="search-field">Search Here</div>
      <div class="search-btn"><svg width="22" height="22" viewBox="0 0 22 22"><circle cx="13" cy="9" r="6.5" fill="none" stroke="#fff" stroke-width="2.5"/><line x1="8" y1="14" x2="2" y2="20" stroke="#fff" stroke-width="3"/></svg></div>
    </div>

    <div class="rail">
      <svg style="top:28px" width="30" height="32" viewBox="0 0 30 32"><circle cx="15" cy="9" r="7" fill="#fff"/><path d="M3 32v-6c0-6 5-9 12-9s12 3 12 9v6z" fill="#fff"/></svg>
      <svg style="top:104px" width="36" height="28" viewBox="0 0 36 28"><circle cx="12" cy="12" r="9" fill="none" stroke="#fff" stroke-width="6" stroke-dasharray="3 2.4"/><circle cx="12" cy="12" r="5" fill="#fff"/><circle cx="12" cy="12" r="2.5" fill="#0a86bf"/><circle cx="28" cy="20" r="5" fill="#fff"/><circle cx="28" cy="20" r="2" fill="#0a86bf"/></svg>
      <svg style="top:174px" width="34" height="34" viewBox="0 0 34 34"><circle cx="17" cy="17" r="14" fill="none" stroke="#fff" stroke-width="6"/><circle cx="17" cy="17" r="5" fill="#fff"/></svg>
      <svg style="top:245px" width="34" height="34" viewBox="0 0 34 34"><path d="M15 4a13 13 0 1 0 13 13H15z" fill="none" stroke="#fff" stroke-width="3"/><path d="M19 0a13 13 0 0 1 13 13H19z" fill="#fff"/></svg>
      <svg style="top:325px" width="32" height="22" viewBox="0 0 32 22"><rect width="32" height="22" fill="#fff"/><path d="M1 2l15 11 15-11" fill="none" stroke="#0a86bf" stroke-width="2"/></svg>
      <svg style="top:396px" width="32" height="32" viewBox="0 0 32 32"><circle cx="16" cy="16" r="15" fill="#fff"/><path d="M11 16a5 5 0 1 0 5-5h-2" fill="none" stroke="#0a86bf" stroke-width="3"/><path d="M13 7l4 4-4 4z" fill="#0a86bf"/></svg>
      <svg style="top:470px" width="30" height="24" viewBox="0 0 30 24"><rect x="1" y="1" width="28" height="22" fill="none" stroke="#fff" stroke-width="2"/><line x1="1" y1="6" x2="29" y2="6" stroke="#fff" stroke-width="2"/><text x="15" y="19" fill="#fff" font-size="10" text-anchor="middle" font-family="Arial">&lt;/&gt;</text></svg>
    </div>

    <div class="tile" style="left:121px;top:210px;background:var(--tile-user)"><span class="badge">15</span><svg width="34" height="34" viewBox="0 0 34 34"><circle cx="17" cy="10" r="7" fill="#fff"/><path d="M6 33v-6c0-6 5-9 11-9s11 3 11 9v6z" fill="#fff"/></svg><span class="label">USER</span></div>
    <div class="tile" style="left:231px;top:210px;background:var(--tile-setting)"><svg width="36" height="34" viewBox="0 0 36 34"><circle cx="13" cy="15" r="8" fill="none" stroke="#fff" stroke-width="6" stroke-dasharray="3 2.4"/><circle cx="13" cy="15" r="5" fill="#fff"/><circle cx="28" cy="23" r="5" fill="#fff"/></svg><span class="label">SETTING</span></div>
    <div class="tile" style="left:121px;top:321px;background:var(--tile-support)"><svg width="34" height="34" viewBox="0 0 34 34"><circle cx="17" cy="17" r="13" fill="none" stroke="#fff" stroke-width="6"/><circle cx="17" cy="17" r="5" fill="#fff"/></svg><span class="label">SUPPORT</span></div>
    <div class="tile" style="left:231px;top:321px;background:var(--tile-events)"><svg width="34" height="36" viewBox="0 0 34 36"><path d="M21 2c-8 6-10 16-7 26l2-1c-1-9 1-17 5-25z" fill="#fff"/><line x1="15" y1="26" x2="13" y2="34" stroke="#fff" stroke-width="2"/></svg><span class="label">EVENTS</span></div>
    <div class="tile" style="left:121px;top:432px;background:var(--tile-graph)"><svg width="34" height="34" viewBox="0 0 34 34"><path d="M15 5a12 12 0 1 0 12 12H15z" fill="none" stroke="#fff" stroke-width="3"/><path d="M19 1a12 12 0 0 1 12 12H19z" fill="#fff"/></svg><span class="label">GRAPH</span></div>
    <div class="tile" style="left:231px;top:432px;background:var(--tile-docs)"><svg width="38" height="28" viewBox="0 0 38 28" style="left:22px"><g fill="none" stroke="#fff" stroke-width="2.5"><rect x="2" y="3" width="10" height="18"/><rect x="14" y="3" width="10" height="18"/><rect x="26" y="3" width="10" height="18"/></g></svg><span class="label compact">DOUCOUMENTS</span></div>
    <div class="tile" style="left:121px;top:543px;background:var(--tile-message)"><svg width="36" height="26" viewBox="0 0 36 26" style="left:23px"><rect width="36" height="24" fill="#fff"/><path d="M1 2l17 12 17-12" fill="none" stroke="#a07400" stroke-width="2"/></svg><span class="label">MASSAGE</span></div>
    <div class="tile" style="left:231px;top:543px;background:var(--tile-source)"><svg width="30" height="26" viewBox="0 0 30 26" style="left:27px"><rect x="1" y="1" width="28" height="22" fill="none" stroke="#fff" stroke-width="2"/><line x1="1" y1="6" x2="29" y2="6" stroke="#fff" stroke-width="2"/><text x="15" y="19" fill="#fff" font-size="10" text-anchor="middle" font-family="Arial">&lt;/&gt;</text></svg><span class="label">SOURCE</span></div>
    <div class="tile" style="left:121px;top:654px;background:var(--tile-refresh)"><svg width="34" height="34" viewBox="0 0 34 34"><circle cx="17" cy="17" r="16" fill="#fff"/><path d="M12 17a5 5 0 1 0 5-5h-2" fill="none" stroke="#470f5c" stroke-width="3"/><path d="M14 8l4 4-4 4z" fill="#470f5c"/></svg><span class="label">REFRESH</span></div>
    <div class="tile" style="left:231px;top:654px;background:var(--tile-library)"><svg width="36" height="34" viewBox="0 0 36 34"><g fill="none" stroke="#fff" stroke-width="2.5"><rect x="2" y="2" width="32" height="28"/><line x1="2" y1="14" x2="34" y2="14"/></g><g fill="#fff"><rect x="8" y="18" width="3" height="10"/><rect x="14" y="18" width="3" height="10"/><rect x="20" y="18" width="3" height="10"/><rect x="26" y="18" width="3" height="10"/></g></svg><span class="label">LIBRARY</span></div>
  </aside>

  <main class="content">
    <h1 class="page-title">Supliar Transactions Screen</h1>
    <div class="rule"></div>
    <div class="crumbs">
      <svg width="18" height="15" viewBox="0 0 18 15"><path d="M9 0l9 8h-3v7h-4v-5H7v5H3V8H0z" fill="#0a86bf"/></svg>
      <span>›</span><span>Login</span><span>›</span><span class="current">Data</span>
    </div>
    <div class="filter">
      <span class="lbl" style="left:7px">Date From</span>
      <div class="date" style="left:92px">8/8/2013<span class="cal"><svg width="16" height="15" viewBox="0 0 16 15"><rect x="1" y="2" width="14" height="12" fill="none" stroke="#fff" stroke-width="1.5"/><rect x="1" y="2" width="14" height="3" fill="#fff"/></svg></span></div>
      <span class="lbl" style="left:277px">Date to</span>
      <div class="date" style="left:362px">9/8/2013<span class="cal"><svg width="16" height="15" viewBox="0 0 16 15"><rect x="1" y="2" width="14" height="12" fill="none" stroke="#fff" stroke-width="1.5"/><rect x="1" y="2" width="14" height="3" fill="#fff"/></svg></span></div>
    </div>
    <div class="grid-bar"></div>
    <table class="grid">
      <colgroup><col style="width:97px"><col style="width:101px"><col style="width:98px"><col style="width:147px"><col style="width:98px"><col style="width:101px"></colgroup>
      <thead><tr><th>DATE</th><th>TYPE</th><th>TIME</th><th>REFRENCE</th><th>AMOUNT</th><th>STETUS</th></tr></thead>
      <tbody>
        <tr><td>03/01/2013</td><td>INV</td><td>03:02 AM</td><td>2548788AAC</td><td>500.00</td><td>RECIVED</td></tr>
        <tr><td>03/01/2013</td><td>PAYMENT</td><td>03:02 AM</td><td>2548788AAC</td><td>100.00</td><td>PAYMENT</td></tr>
        <tr><td>03/01/2013</td><td>PAYMENT</td><td>03:02 AM</td><td>2548788AAC</td><td>100.00</td><td>PAYMENT</td></tr>
        <tr><td>03/01/2013</td><td>PAYMENT</td><td>03:02 AM</td><td>2548788AAC</td><td>100.00</td><td>PAYMENT</td></tr>
        <tr><td>03/01/2013</td><td>PAYMENT</td><td>03:02 AM</td><td>2548788AAC</td><td>100.00</td><td>PAYMENT</td></tr>
        <tr><td>03/01/2013</td><td>INV</td><td>03:02 AM</td><td>2548788AAC</td><td>500.00</td><td>RECIVED</td></tr>
        <tr><td>03/01/2013</td><td>INV</td><td>03:02 AM</td><td>2548788AAC</td><td>500.00</td><td>RECIVED</td></tr>
        <tr><td>03/01/2013</td><td>INV</td><td>03:02 AM</td><td>2548788AAC</td><td>500.00</td><td>RECIVED</td></tr>
        <tr><td>03/01/2013</td><td>INV</td><td>03:02 AM</td><td>2548788AAC</td><td>500.00</td><td>RECIVED</td></tr>
        <tr><td>03/01/2013</td><td>INV</td><td>03:02 AM</td><td>2548788AAC</td><td>500.00</td><td>RECIVED</td></tr>
        <tr><td>03/01/2013</td><td>INV</td><td>03:02 AM</td><td>2548788AAC</td><td>500.00</td><td>RECIVED</td></tr>
        <tr><td>03/01/2013</td><td>INV</td><td>03:02 AM</td><td>2548788AAC</td><td>500.00</td><td>RECIVED</td></tr>
        <tr><td>03/01/2013</td><td>INV</td><td>03:02 AM</td><td>2548788AAC</td><td>500.00</td><td>RECIVED</td></tr>
        <tr><td>03/01/2013</td><td>INV</td><td>03:02 AM</td><td>2548788AAC</td><td>500.00</td><td>RECIVED</td></tr>
        <tr><td>03/01/2013</td><td>INV</td><td>03:02 AM</td><td>2548788AAC</td><td>500.00</td><td>RECIVED</td></tr>
      </tbody>
    </table>
    <div class="pager">
      <span class="count">1-2 OF 2 ITEMS</span>
      <span class="pbtn" style="left:469px"><svg width="14" height="10" viewBox="0 0 14 10"><path d="M6 0L1 5l5 5M13 0L8 5l5 5" fill="none" stroke="#fff" stroke-width="2.2"/></svg></span>
      <span class="pbtn dim" style="left:504px"><svg width="8" height="10" viewBox="0 0 8 10"><path d="M6 0L1 5l5 5" fill="none" stroke="#bbb" stroke-width="2"/></svg></span>
      <span class="pbtn page" style="left:538px">2</span>
      <span class="pbtn dim" style="left:574px"><svg width="8" height="10" viewBox="0 0 8 10"><path d="M2 0l5 5-5 5" fill="none" stroke="#bbb" stroke-width="2"/></svg></span>
      <span class="pbtn" style="left:607px"><svg width="14" height="10" viewBox="0 0 14 10"><path d="M1 0l5 5-5 5M8 0l5 5-5 5" fill="none" stroke="#fff" stroke-width="2.2"/></svg></span>
    </div>
    <footer class="footer">COPYRIGHT © 2013 LUMEO. ALL PAGES OF THE WEBSITE ARE SUBJECT TO OUR TERMS AND CONDITIONS AND PRIVACY POLICY.</footer>
  </main>
</div>
</body>
</html>
```